National wood flooring liquidator needs flyer

Need a flyer to provide house flippers, home builders, and home remodlers to call us on below wholesale wood flooring overstocks, dicontinues and one of a kinds that may be available in their area of the U.S. Availabilities in styles and quantities change daily and weekly and sell on 1st come basis.

Target Market(s)

house flippers, home builders, and home remodlers

Industry/Entity Type

Flooring

Number of Pages Required

1 page

Requirements
Must have
• Wood flooring only, 3/4" thick solid and engineered
Nice to have
• 4 color photos of wood flooring room scenes
Should not have
• No laminate, carpet or vinyl

```html
<!DOCTYPE html>
<html lang="en">
<head>
<meta charset="utf-8">
<title>Wood Flooring Flyer</title>
<link href="https://fonts.googleapis.com/css2?family=Cinzel:wght@400;600&family=Advent+Pro:wght@300;400&family=Exo+2:wght@500;800&family=Abril+Fatface&display=swap" rel="stylesheet">
<style>
  :root{
    --wood-dark:#5a3b26;
    --wood-mid:#7a5238;
    --wood-light:#8d6043;
    --panel:rgba(52,33,18,0.86);
    --orange:#e2560f;
    --orange-deep:#e06512;
    --orange-rim:#f28c10;
    --amber:#f2a12c;
    --red:#e8201a;
    --stamp:#e3231b;
    --yellow:#ffd23a;
    --white:#ffffff;
  }
  *{margin:0;padding:0;box-sizing:border-box}
  html,body{width:846px;height:1200px;overflow:hidden;background:#fff}
  .flyer{position:relative;width:846px;height:1200px;overflow:hidden}
  .wood-bg{position:absolute;inset:0;
    background:
      linear-gradient(90deg,rgba(0,0,0,.10) 0 1px,transparent 1px 100%) 0 0/110px 100%,
      linear-gradient(180deg,var(--wood-mid) 0%,var(--wood-light) 45%,var(--wood-mid) 75%,var(--wood-dark) 100%);}
  .title-band{position:absolute;left:0;top:149px;width:680px;height:129px;background:var(--orange-rim)}
  .title-band .inner{position:absolute;left:0;top:15px;width:665px;height:99px;
    background:linear-gradient(90deg,#dd4f10,var(--orange-deep) 60%,#e8720f)}
  .title{position:absolute;left:32px;top:160px;font-family:"Cinzel",serif;font-weight:400;
    font-size:80px;line-height:1;color:var(--white);letter-spacing:1px;white-space:nowrap;
    text-shadow:2px 3px 3px rgba(0,0,0,.35)}
  .title .sc{font-size:62px}
  .features-panel{position:absolute;left:0;top:465px;width:518px;height:472px;background:var(--panel)}
  .feature-lines{position:absolute;left:0;top:0}
  .feature{position:absolute;left:28px;font-family:"Advent Pro",sans-serif;font-weight:300;
    font-size:29px;line-height:1;color:var(--white);white-space:nowrap;letter-spacing:.5px}
  .stamp{position:absolute;left:520px;top:452px}
  .company-box{position:absolute;left:367px;top:937px;width:479px;height:263px;background:var(--orange)}
  .company{position:absolute;left:0;right:0;top:braid;top:30px;text-align:center;padding-left:20px;
    font-family:"Advent Pro",sans-serif;font-weight:300;font-size:52px;line-height:1;color:var(--white);white-space:nowrap}
  .rule{position:absolute;left:44px;width:417px;height:1px;background:rgba(255,255,255,.8)}
  .notice{position:absolute;left:94px;top:126px;width:314px;height:81px;background:var(--red);
    text-align:center;font-family:"Advent Pro",sans-serif;font-size:22px;line-height:26px;color:var(--white);padding-top:3px}
  .notice .cta{font-family:"Exo 2",sans-serif;font-weight:800;color:var(--yellow);font-size:20px}
  .phone-band{position:absolute;left:15px;top:207px;width:454px;height:56px;background:var(--amber);
    font-family:"Exo 2",sans-serif;font-weight:500;font-size:29px;color:var(--white);
    line-height:56px;text-align:center;white-space:nowrap}
</style>
</head>
<body>
<main class="flyer">
  <div class="wood-bg" role="img" aria-label="Warm brown hardwood plank flooring texture"></div>

  <header class="title-band"><div class="inner"></div></header>
  <h1 class="title">W<span class="sc">OOD</span> F<span class="sc">LOORING</span></h1>

  <section class="features-panel">
    <svg class="feature-lines" width="518" height="472" viewBox="0 0 518 472" fill="none" stroke="#fff" stroke-width="2">
      <path d="M514 66V472"/>
      <path d="M31 66H514M31 66V83H111"/>
      <path d="M31 146H514M31 146V163H111"/>
      <path d="M31 216H514M31 216V233H111"/>
      <path d="M31 287H514M31 287V304H111"/>
      <path d="M31 354H514M31 354V371H111"/>
      <path d="M31 432H514M31 432V449H111"/>
    </svg>
    <p class="feature" style="top:32px">Wood Flooring ONLY</p>
    <p class="feature" style="top:112px">Solid and Engineered</p>
    <p class="feature" style="top:182px">Factory PRE-finished</p>
    <p class="feature" style="top:252px">Available in Various Styles</p>
    <p class="feature" style="top:321px">3/8" to 3/4" thick</p>
    <p class="feature" style="top:398px">Quantities change Daily and Weekly</p>
  </section>

  <svg class="stamp" width="330" height="330" viewBox="0 0 330 330" aria-label="First come basis">
    <defs>
      <linearGradient id="stampText" x1="0" y1="0" x2="0" y2="1">
        <stop offset="0" stop-color="#fff3b0"/>
        <stop offset="1" stop-color="#ffcc33"/>
      </linearGradient>
    </defs>
    <circle cx="166" cy="165" r="160" fill="var(--stamp)" opacity=".92"/>
    <circle cx="166" cy="165" r="143" fill="none" stroke="#8a4a2e" stroke-width="4" opacity=".8"/>
    <circle cx="166" cy="165" r="133" fill="#e4231a"/>
    <g transform="rotate(-32 166 165)" fill="url(#stampText)" font-family="'Abril Fatface',serif" text-anchor="middle">
      <text x="160" y="115" font-size="46" letter-spacing="2">FIRST</text>
      <text x="166" y="180" font-size="70" letter-spacing="1">COME</text>
      <text x="172" y="240" font-size="62" letter-spacing="3">BASIS</text>
    </g>
  </svg>

  <footer class="company-box">
    <p class="company">Timberline Stock Co.</p>
    <div class="rule" style="top:90px"></div>
    <div class="rule" style="top:107px"></div>
    <div class="notice">
      Quantities will not last long.<br>
      Don’t miss the opportunity.<br>
      <span class="cta">CALL US NOW!</span>
    </div>
    <div class="phone-band">Toll Free at 1-800-555-0148</div>
  </footer>
</main>
</body>
</html>
```